Bright Arc Electrical & Communications business card design

We would like a double sided business card that is different. Want it to be exciting and fun. Something that people keep rather then just throw it in the bin.
We have a logo that we want to put on one side of the business card and then the business information on the reverse side. Trying to go for a real professional style of business card

Target Market(s)

Electrical

Industry/Entity Type

Electrical

Contact Information for Business Card

Bright Arc Electrical & Communications
Marcus Trelowen
P: 0437 286 354
E: brightarc@mailrove.com.au
Lic No: 547106K
24/7

Font styles to use
Other font styles liked:
• Would like ideas

Requirements
Must have
• Our company logo (preferably on both sides) yellow needs to be incorporated somewhere. Business card card colours to match with logo. Maybe a small pop of colour
Nice to have
• Open to some design ideas

```html
<!DOCTYPE html>
<html lang="en">
<head>
<meta charset="utf-8">
<title>Bright Arc Electrical &amp; Communications – Business Card</title>
<link href="https://fonts.googleapis.com/css2?family=Michroma&family=Open+Sans:wght@400;600;700&display=swap" rel="stylesheet">
<style>
  :root {
    --bg: #e9e7e3;
    --card-white: #ffffff;
    --ink: #111111;
    --grey-light: #b9b9b9;
    --grey-mid: #8a8a8a;
    --grey-dark: #4d4d4d;
    --yellow: #fff200;
    --yellow-line: #f2d21b;
    --brand-grey: #6e6e6e;
  }
  html, body {
    margin: 0;
    padding: 0;
    width: 1200px;
    height: 913px;
    overflow: hidden;
    background: var(--bg);
  }
  .canvas {
    position: relative;
    width: 1200px;
    height: 913px;
  }
  .card {
    position: absolute;
    width: 560px;
    height: 320px;
    border-radius: 20px;
    overflow: hidden;
    box-shadow: 0 10px 28px rgba(0,0,0,0.18);
  }
  /* Front: company details */
  .card-front {
    left: 50px;
    top: 110px;
    background: var(--card-white);
  }
  .front-swoosh {
    position: absolute;
    inset: 0;
  }
  .company-name {
    position: absolute;
    left: 30px;
    top: 72px;
    margin: 0;
    font-family: "Michroma", sans-serif;
    font-weight: 400;
    font-size: 20px;
    letter-spacing: 0.3px;
    color: var(--ink);
    line-height: 1;
    white-space: nowrap;
  }
  .company-tagline {
    position: absolute;
    left: 30px;
    top: 100px;
    width: 345px;
    display: flex;
    align-items: center;
    gap: 8px;
    font-family: "Michroma", sans-serif;
    font-size: 10px;
    color: var(--ink);
    white-space: nowrap;
  }
  .company-tagline .rule {
    flex: 1;
    height: 2px;
    background: var(--yellow-line);
  }
  .hours-badge {
    position: absolute;
    left: 34px;
    top: 238px;
    width: 40px;
    height: 40px;
    border: 2px solid var(--ink);
    border-radius: 50%;
    box-sizing: border-box;
    display: flex;
    align-items: center;
    justify-content: center;
    font-family: "Open Sans", sans-serif;
    font-weight: 700;
    font-size: 12px;
    color: var(--ink);
  }
  .contact {
    position: absolute;
    right: 24px;
    top: 168px;
    text-align: right;
    font-family: "Open Sans", sans-serif;
    color: #ffffff;
  }
  .contact-name {
    margin: 0;
    font-size: 16px;
    font-weight: 700;
  }
  .contact-role {
    margin: 1px 0 4px;
    font-size: 11px;
  }
  .contact-line {
    margin: 2px 0;
    font-size: 12px;
    display: flex;
    justify-content: flex-end;
    align-items: center;
    gap: 6px;
  }
  .contact-line svg {
    width: 11px;
    height: 11px;
  }
  /* Back: brand side */
  .card-back {
    left: 590px;
    top: 480px;
    background: var(--yellow);
    display: flex;
    align-items: center;
    justify-content: center;
  }
  .brand-name {
    font-family: "Open Sans", sans-serif;
    font-weight: 700;
    font-size: 40px;
    color: var(--brand-grey);
  }
</style>
</head>
<body>
<main class="canvas">

  <section class="card card-front" aria-label="Business card front">
    <svg class="front-swoosh" viewBox="0 0 560 320" preserveAspectRatio="none" aria-hidden="true">
      <defs>
        <linearGradient id="greyPanel" x1="0" y1="0" x2="1" y2="1">
          <stop offset="0" stop-color="#b9b9b9"/>
          <stop offset="0.5" stop-color="#8a8a8a"/>
          <stop offset="1" stop-color="#4d4d4d"/>
        </linearGradient>
      </defs>
      <path d="M440,0 C430,140 330,260 220,320 L560,320 L560,0 Z" fill="url(#greyPanel)"/>
      <path d="M418,70 C408,180 320,272 196,320 L214,320 C318,266 404,178 418,70 Z" fill="#111111"/>
    </svg>

    <h1 class="company-name">BRIGHT ARC ELECTRICAL</h1>
    <div class="company-tagline"><span class="rule"></span><span>&amp; COMMUNICATIONS</span><span class="rule"></span></div>

    <div class="hours-badge">24/7</div>

    <div class="contact">
      <p class="contact-name">Marcus Trelowen</p>
      <p class="contact-role">Electrician</p>
      <p class="contact-line">Lic No: 547106K</p>
      <p class="contact-line">0437 286 354
        <svg viewBox="0 0 24 24" aria-hidden="true"><path fill="#fff200" d="M6.6 10.8a15.1 15.1 0 0 0 6.6 6.6l2.2-2.2c.3-.3.7-.4 1-.2 1.1.4 2.3.6 3.6.6.6 0 1 .4 1 1V20c0 .6-.4 1-1 1A17 17 0 0 1 3 4c0-.6.4-1 1-1h3.5c.6 0 1 .4 1 1 0 1.3.2 2.5.6 3.6.1.3 0 .7-.2 1z"/></svg>
      </p>
      <p class="contact-line">brightarc@mailrove.com.au
        <svg viewBox="0 0 24 24" aria-hidden="true"><rect x="2" y="5" width="20" height="14" rx="2" fill="none" stroke="#fff200" stroke-width="2"/><path d="M3 6l9 7 9-7" fill="none" stroke="#fff200" stroke-width="2"/></svg>
      </p>
    </div>
  </section>

  <section class="card card-back" aria-label="Business card back">
    <span class="brand-name">Bright Arc</span>
  </section>

</main>
</body>
</html>
```